Business card design for Automotive workshop

We need a business card for a new automotive repair and tyre shop called Ridgeback Prime Automotive located in New Zealand. We are a clean, modern and fresh workshop and company.

Front needs to feature logo,
my name:
Lachie Westergaard (director)

Address:
48 Marlow Lane
Kereru Bay 3591

Phone: 07 842 1937
Mobile: 027 519 2764
Email: office@ridgebackmotors.co.nz
Website: ridgebackmotors.co.nz

Back needs to feature an area to write down appointment details, date and time.

Also feature a list of jobs and work we do such as,
Vehicle Servicing
All Mechanical Repairs
Warrant of Fitness
Tyres & Wheel Alignments
Automotive Diagnostics
Automotive Parts & Supplies

```html
<!DOCTYPE html>
<html lang="en">
<head>
<meta charset="utf-8">
<title>Ridgeback Prime Automotive – Business Card</title>
<link href="https://fonts.googleapis.com/css2?family=Roboto:wght@400;500;700&display=swap" rel="stylesheet">
<style>
  :root {
    --stage: #2b2b2b;
    --card-dark: #1f1f1f;
    --card-light: #ffffff;
    --red: #e21b23;
    --ink: #1a1a1a;
    --white: #ffffff;
    --muted: #d9d9d9;
  }
  * { box-sizing: border-box; margin: 0; padding: 0; }
  html, body {
    width: 1200px; height: 895px; overflow: hidden;
    background: var(--stage);
    font-family: "Roboto", Arial, sans-serif;
  }
  .canvas { position: relative; width: 1200px; height: 895px; }
  .card {
    position: absolute; width: 560px; height: 320px; overflow: hidden;
    box-shadow: 0 14px 30px rgba(0,0,0,.45);
  }

  /* Back: appointment card */
  .card-back { left: 70px; top: 70px; background: var(--card-light); color: var(--ink); }
  .appointment {
    position: absolute; left: 40px; right: 40px; top: 34px;
    display: flex; gap: 14px; font-size: 13px; align-items: flex-end;
  }
  .appointment .field { display: flex; align-items: flex-end; gap: 6px; }
  .appointment .field.date { flex: 1.4; }
  .appointment .field.time { flex: 1; }
  .appointment .rule { flex: 1; border-bottom: 1px solid var(--ink); height: 1px; margin-bottom: 3px; }
  .brand {
    display: flex; align-items: center; gap: 10px;
    color: var(--red); font-weight: 700; letter-spacing: .5px; white-space: nowrap;
  }
  .brand .mark { width: 14px; height: 14px; background: var(--red); flex: none; }
  .card-back .brand { position: absolute; left: 0; right: 0; top: 100px; justify-content: center; font-size: 30px; }
  .services {
    position: absolute; left: 60px; right: 40px; top: 170px;
    display: grid; grid-template-columns: 1fr 1fr; column-gap: 20px;
  }
  .services ul { list-style: none; }
  .services li {
    font-size: 13.5px; line-height: 22px; display: flex; align-items: center; gap: 10px;
  }
  .services li::before {
    content: ""; width: 7px; height: 7px; border: 2px solid var(--red); border-radius: 50%; flex: none;
  }
  .web-band {
    position: absolute; left: 0; right: 0; bottom: 0; height: 40px;
    background: var(--card-dark); color: var(--white);
    display: flex; align-items: center; justify-content: center;
    font-size: 14px; font-weight: 500; letter-spacing: .4px;
  }
  .web-band .domain { color: var(--red); }

  /* Front: contact card */
  .card-front { left: 570px; top: 505px; background: var(--card-dark); color: var(--white); }
  .card-front .brand { position: absolute; left: 0; right: 0; top: 46px; justify-content: center; font-size: 28px; }
  .person { position: absolute; right: 286px; top: 138px; text-align: right; white-space: nowrap; }
  .person .name { color: var(--red); font-weight: 700; font-size: 20px; letter-spacing: .5px; text-transform: uppercase; }
  .person .role { font-size: 14px; margin-top: 4px; }
  .divider { position: absolute; left: 290px; top: 118px; width: 1px; height: 86px; background: var(--muted); }
  .contacts { position: absolute; left: 306px; top: 118px; list-style: none; }
  .contacts li { display: flex; align-items: center; gap: 8px; font-size: 13px; line-height: 21.5px; white-space: nowrap; }
  .contacts svg { width: 12px; height: 12px; flex: none; }
  .address-band {
    position: absolute; left: 150px; right: 110px; bottom: 38px; height: 32px;
    background: var(--red); display: flex; align-items: center; justify-content: center;
    font-size: 15px; font-weight: 500; white-space: nowrap;
  }
  .stripes { position: absolute; width: 140px; height: 40px; }
  .stripes.left { left: -10px; bottom: 26px; }
  .stripes.right { right: -10px; bottom: 74px; }
</style>
</head>
<body>
<main class="canvas">

  <section class="card card-back" aria-label="Appointment card">
    <div class="appointment">
      <div class="field date"><span>Date:</span><span class="rule"></span></div>
      <div class="field time"><span>Time:</span><span class="rule"></span></div>
    </div>
    <div class="brand"><span class="mark"></span>Ridgeback Prime Automotive</div>
    <div class="services">
      <ul>
        <li>Vehicle Servicing</li>
        <li>All Mechanical Repairs</li>
        <li>Warrant of Fitness</li>
      </ul>
      <ul>
        <li>Tyres &amp; Wheel Alignments</li>
        <li>Automotive Diagnostics</li>
        <li>Automotive Parts &amp; Supplies</li>
      </ul>
    </div>
    <div class="web-band">www.<span class="domain">ridgebackmotors</span>.co.nz</div>
  </section>

  <section class="card card-front" aria-label="Contact card">
    <div class="brand"><span class="mark"></span>Ridgeback Prime Automotive</div>
    <div class="person">
      <p class="name">Lachie Westergaard</p>
      <p class="role">Director</p>
    </div>
    <div class="divider"></div>
    <ul class="contacts">
      <li><svg viewBox="0 0 24 24" fill="none" stroke="#e21b23" stroke-width="2.4"><path d="M5 3h4l2 5-3 2a12 12 0 0 0 6 6l2-3 5 2v4a2 2 0 0 1-2 2A18 18 0 0 1 3 5a2 2 0 0 1 2-2z"/></svg>07 842 1937</li>
      <li><svg viewBox="0 0 24 24" fill="none" stroke="#e21b23" stroke-width="2.4"><rect x="6" y="2" width="12" height="20" rx="2"/><path d="M11 18h2"/></svg>027 519 2764</li>
      <li><svg viewBox="0 0 24 24" fill="none" stroke="#e21b23" stroke-width="2.4"><rect x="2" y="5" width="20" height="14" rx="1"/><path d="M2 6l10 7 10-7"/></svg>office@ridgebackmotors.co.nz</li>
      <li><svg viewBox="0 0 24 24" fill="none" stroke="#e21b23" stroke-width="2.4"><circle cx="10" cy="10" r="7"/><path d="M15 15l6 6"/></svg>ridgebackmotors.co.nz</li>
    </ul>
    <svg class="stripes left" viewBox="0 0 140 40" aria-hidden="true">
      <polygon points="0,30 120,0 140,0 20,30" fill="#fff"/>
      <polygon points="30,40 140,12 140,20 50,40" fill="#fff"/>
    </svg>
    <div class="address-band">48 Marlow Lane, Kereru Bay 3591</div>
    <svg class="stripes right" viewBox="0 0 140 40" aria-hidden="true">
      <polygon points="0,22 140,0 140,8 20,22" fill="#fff"/>
      <polygon points="10,40 140,18 140,28 40,40" fill="#fff"/>
    </svg>
  </section>

</main>
</body>
</html>
```